Website for new slot-booking/reservations website/software

For a new software product we need a brand new logo and website for a reservations/booking system. The website should ideally present the main features with information text, contact info, news page as well as registration and pricing pages. As currently primary field of operation the software should be used for tennis but later on, also for other sport types. Also we'd like to be the logo a text-brand which includes the name "feldreserva.net" or just "feldreserva". The logo should ideally include an icon-design in some way. Generally we are open for ideas.

Bootstrap 4 template is a minimum requirement. (Multi-Page preferred, Single-Page still OK.)

You can use the attached image as an inspiration, but change of colors or other design elements are up to you. Currently the application has a primary color of #5500ff. The website created by you will not include the application itself, so it can have different (but ideally similar) Look&Feel.

Target Market(s)

Sports, Club-Management

Logo Text

feldreserva.net

Coding

Coded - Design and coding required

Number of Pages Required

5+ page

Font styles to use
Sans Serif

Requirements
Must have
• Bootstrap 4 Template, SCSS
Nice to have
• Rapid Loading Times, not too much external JS Libraries.
Should not have
• Extensive animations

```html
<!DOCTYPE html>
<html lang="en">
<head>
<meta charset="utf-8">
<title>Feldreserva – Court Booking Software</title>
<link rel="stylesheet" href="https://fonts.googleapis.com/css2?family=Oswald:wght@500;700&family=Poppins:wght@400;500&display=swap">
<style>
:root{
  --brand:#5500ff;
  --ink:#1a1a1a;
  --text:#333;
  --grey:#6b6b6b;
  --soft:#f6f6f6;
  --dark:#3e3e40;
  --white:#fff;
}
*{box-sizing:border-box;margin:0;padding:0}
html,body{width:1200px;height:3663px;overflow:hidden}
body{position:relative;background:var(--white);font-family:"Poppins",sans-serif;color:var(--text)}
.abs{position:absolute}
.heading{font-family:"Oswald",sans-serif;font-weight:700;color:var(--brand);text-transform:uppercase;letter-spacing:.5px}
.btn{position:absolute;display:flex;align-items:center;justify-content:center;background:var(--brand);color:var(--white);font-family:"Poppins",sans-serif;font-weight:500;text-transform:uppercase;text-decoration:none}
.copy{font-size:12.5px;line-height:21.5px;color:var(--text)}

/* header */
.site-header{position:absolute;top:0;left:0;width:1200px;height:86px;background:var(--white);z-index:3}
.brand{position:absolute;left:172px;top:24px;display:flex;align-items:center;gap:8px}
.brand-dot{width:28px;height:28px;border-radius:50%;background:var(--brand)}
.brand-name{font-family:"Oswald",sans-serif;font-weight:700;font-size:24px;color:var(--ink);text-transform:uppercase}
.nav a{position:absolute;top:42px;font-size:12.5px;font-weight:500;color:var(--ink);text-decoration:none}
.nav a.active{color:var(--brand)}
.nav a.register{top:28px;left:938px;width:89px;height:43px;font-size:12.5px;color:var(--white)}

/* hero */
.hero{position:absolute;top:86px;left:0;width:1200px;height:640px;overflow:hidden}
.hero-photo{position:absolute;inset:0;background:linear-gradient(180deg,#7fa7c4 0%,#a9bfcc 38%,#b7825a 62%,#8a4f2c 100%)}
.hero-cut{position:absolute;inset:0}
.hero-title{position:absolute;left:171px;top:144px;font-family:"Oswald",sans-serif;font-weight:700;font-size:56px;color:var(--white);text-transform:uppercase}
.hero-text{position:absolute;left:172px;top:244px;width:520px;font-size:12.5px;line-height:21px;color:var(--white)}
.hero .btn{left:172px;top:332px;width:159px;height:64px;font-size:16px}
.app-phone{position:absolute;left:967px;top:241px;width:168px;height:363px;border-radius:14px;background:linear-gradient(180deg,#2d2f70,#151638);border:3px solid #111}

/* about */
.about-title{position:absolute;top:780px;width:1200px;text-align:center;font-size:40px}
.about-lead{position:absolute;top:842px;left:175px;width:830px;text-align:center}
.timeline{position:absolute;left:221px;top:921px;width:2px;height:427px;background:var(--ink)}
.timeline::before,.timeline::after{content:"";position:absolute;left:-3px;width:8px;height:8px;border-radius:50%;background:var(--ink)}
.timeline::before{top:-4px}.timeline::after{bottom:-4px}
.step{position:absolute;border-radius:50%;display:flex;align-items:center;justify-content:center;box-shadow:3px 4px 6px rgba(0,0,0,.25);border:3px solid var(--white)}
.step.brand-fill{background:var(--brand)}
.step.grey-fill{background:var(--grey)}
.step-text{position:absolute;left:279px;width:370px;font-size:13px;line-height:21.5px;color:var(--text)}
.about-art{position:absolute;left:675px;top:988px;width:441px;height:306px;background:linear-gradient(160deg,#e23b3b 0%,#2fa84a 45%,#1d2f5e 100%);border-radius:20px}

/* software */
.software{position:absolute;top:1422px;left:0;width:1200px;height:621px;background:var(--soft)}
.software-art{position:absolute;left:0;top:156px;width:597px;height:341px;background:linear-gradient(160deg,#ffffff 0%,#e9e6f5 45%,#1f2b55 100%);border-radius:0 30px 60px 0}
.software-title{position:absolute;left:630px;top:106px;font-size:42px}
.software-body{position:absolute;left:630px;top:175px;width:398px;display:flex;flex-direction:column;gap:19px}
.software-body .copy,.contact-copy{font-size:12px;text-align:justify}
.software .btn{left:630px;top:421px;width:122px;height:48px;font-size:13px}

/* contact */
.contact-title{position:absolute;left:172px;top:2108px;font-size:42px}
.contact-body{position:absolute;left:172px;top:2173px;width:398px;display:flex;flex-direction:column;gap:18px}
.contact-link{font-size:13.5px;color:var(--brand)}
.contact-more{left:173px;top:2349px;width:123px;height:50px;font-size:13.5px}
.contact-photo{position:absolute;left:593px;top:2043px;width:607px;height:442px;background:linear-gradient(160deg,#6a4a34 0%,#a8652e 45%,#7a3a18 100%);clip-path:polygon(65px 0,100% 0,100% 100%,0 100%)}
.field{position:absolute;border:2px solid var(--white);color:var(--white);font-size:14px;padding-left:10px;display:flex;align-items:center}
.submit{left:681px;top:2278px;width:114px;height:55px;font-size:17px}

/* pricing */
.pricing-title{position:absolute;top:2582px;width:1200px;text-align:center;font-size:42px}
.plan{position:absolute;top:2689px;width:265px;height:428px}
.plan::before{content:"";position:absolute;left:0;top:0;right:0;height:122px;border:5px solid var(--ink);border-bottom:none}
.plan.featured::before{border-color:var(--brand)}
.plan-card{position:absolute;left:7px;right:7px;top:5px;bottom:0;background:var(--white);box-shadow:0 3px 10px rgba(0,0,0,.12);border-bottom:4px solid var(--grey);text-align:center}
.plan.featured .plan-card{border-bottom-color:var(--brand)}
.plan-name{margin-top:22px;font-family:"Oswald",sans-serif;font-weight:700;font-size:34px;color:var(--ink);text-transform:uppercase}
.price{display:inline-block;margin-top:10px;padding:0 12px;height:54px;line-height:50px;border:2px solid var(--ink);font-family:"Oswald",sans-serif;font-weight:700;font-size:27px;color:var(--ink)}
.plan.featured .plan-name{color:var(--brand)}
.plan.featured .price{background:var(--brand);border-color:var(--brand);color:var(--white)}
.plan-copy{margin:22px auto 0;width:224px;font-size:11.5px;line-height:21.5px}
.plan-points{margin-top:14px;font-family:"Oswald",sans-serif;font-weight:500;font-size:14.5px;line-height:22px;color:var(--ink);text-transform:uppercase}
.plan.featured .plan-points{color:var(--brand)}

/* footer */
.site-footer{position:absolute;top:3190px;left:0;width:1200px;height:473px}
.contact-item{position:absolute;display:flex;gap:14px;font-family:"Oswald",sans-serif;font-weight:500;font-size:14.5px;line-height:22.5px;color:var(--white);text-transform:uppercase}
.contact-item svg{flex:none}
.footer-rule{position:absolute;left:172px;top:374px;width:855px;height:1px;background:#6d6d70}
.copyright{position:absolute;top:405px;width:1200px;text-align:center;font-family:"Oswald",sans-serif;font-weight:500;font-size:14px;color:var(--white);text-transform:uppercase}
</style>
</head>
<body>

<header class="site-header">
  <div class="brand"><span class="brand-dot"></span><span class="brand-name">Feldreserva</span></div>
  <nav class="nav">
    <a class="active" style="left:470px">HOME</a>
    <a style="left:537px">ABOUT</a>
    <a style="left:610px">FEATURES</a>
    <a style="left:708px">PRICING</a>
    <a style="left:789px">NEWS</a>
    <a style="left:855px">CONTACT</a>
    <a class="btn register">Register</a>
  </nav>
</header>

<section class="hero">
  <div class="hero-photo" role="img" aria-label="Tennis player lunging for a ball on a clay court"></div>
  <svg class="hero-cut" width="1200" height="640" viewBox="0 0 1200 640">
    <polygon points="0,618 1200,540 1200,561 0,639" fill="#5500ff"/>
    <polygon points="0,639 1200,561 1200,640 0,640" fill="#fff"/>
  </svg>
  <h1 class="hero-title">Feldreserva</h1>
  <p class="hero-text">Nemo enim ipsam voluptatem quia voluptas sit aspernatur aut odit aut fugit, sed quia consequuntur magni dolores.</p>
  <a class="btn">Get Software</a>
  <div class="app-phone" role="img" aria-label="Phone showing the tennis coaching app with stroke categories"></div>
</section>

<h2 class="heading about-title">About Us</h2>
<p class="copy about-lead">Nam libero tempore, cum soluta nobis est eligendi optio cumque nihil impedit quo minus id quod maxime placeat facere possimus, omnis voluptas assumenda est, omnis dolor repellendus.</p>

<div class="timeline"></div>
<div class="step brand-fill" style="left:191px;top:945px;width:60px;height:60px"><svg width="26" height="30" viewBox="0 0 26 30"><circle cx="13" cy="11" r="9" fill="none" stroke="#fff" stroke-width="3"/><rect x="10.5" y="19" width="5" height="10" rx="2" fill="#fff"/></svg></div>
<div class="step grey-fill" style="left:185px;top:1028px;width:72px;height:72px"><svg width="30" height="36" viewBox="0 0 26 30"><circle cx="13" cy="11" r="9" fill="none" stroke="#fff" stroke-width="3"/><rect x="10.5" y="19" width="5" height="10" rx="2" fill="#fff"/></svg></div>
<div class="step brand-fill" style="left:177px;top:1119px;width:88px;height:88px"><svg width="36" height="42" viewBox="0 0 26 30"><circle cx="13" cy="11" r="9" fill="none" stroke="#fff" stroke-width="3"/><rect x="10.5" y="19" width="5" height="10" rx="2" fill="#fff"/></svg></div>
<div class="step grey-fill" style="left:174px;top:1230px;width:94px;height:94px"><svg width="38" height="44" viewBox="0 0 26 30"><circle cx="13" cy="11" r="9" fill="none" stroke="#fff" stroke-width="3"/><rect x="10.5" y="19" width="5" height="10" rx="2" fill="#fff"/></svg></div>
<p class="step-text" style="top:953px">At vero eos et accusamus et iusto odio dignissimos ducimus qui blanditiis praesentium</p>
<p class="step-text" style="top:1043px">At vero eos et accusamus et iusto odio dignissimos ducimus qui blanditiis praesentium</p>
<p class="step-text" style="top:1140px">At vero eos et accusamus et iusto odio dignissimos ducimus qui blanditiis praesentium</p>
<p class="step-text" style="top:1264px">At vero eos et accusamus et iusto odio dignissimos ducimus qui blanditiis praesentium</p>
<div class="about-art" role="img" aria-label="Isometric phone with a table tennis court and a watch online badge"></div>

<section class="software">
  <div class="software-art" role="img" aria-label="Isometric laptop screen showing the booking dashboard with charts"></div>
  <h2 class="heading software-title">Our Software</h2>
  <div class="software-body">
    <p class="copy">Nam libero tempore, cum soluta nobis est eligendi optio cumque nihil impedit quo minus id quod maxime placeat facere possimus, omnis voluptas assumenda est, omnis dolor repellendus. Temporibus autem quibusdam et aut officiis debitis aut rerum ne cessitatibus saepe eveniet ut et voluptates.</p>
    <p class="copy">At vero eos et accusamus et iusto odio dignissimos ducimus qui blanditiis praesentium voluptatum deleniti atque corrupti quos do lores et quas molestias excepturi sint occaecati cupiditate non provident, similique sunt.</p>
  </div>
  <a class="btn">Our Screens</a>
</section>

<h2 class="heading contact-title">Contact Form</h2>
<div class="contact-body">
  <p class="copy contact-copy">Nam libero tempore, cum soluta nobis est eligendi optio cumque nihil impedit quo minus id quod maxime placeat facere possimus, omnis voluptas assumenda est, omnis dolor repellendus. Temporibus autem quibusdam et aut officiis debitis aut rerum ne cessitatibus saepe eveniet ut et voluptates.</p>
  <p class="contact-link">Nam libero tempore, cum soluta nobis est eligendis</p>
</div>
<a class="btn contact-more">Read More</a>
<div class="contact-photo" role="img" aria-label="Tennis player holding a racket and ball on a sunset court"></div>
<div class="field" style="left:681px;top:2127px;width:166px;height:55px">Name</div>
<div class="field" style="left:860px;top:2127px;width:167px;height:55px">Phone</div>
<div class="field" style="left:681px;top:2202px;width:346px;height:56px">Email</div>
<a class="btn submit">Submit</a>

<h2 class="heading pricing-title">Our Pricing</h2>
<div class="plan" style="left:172px">
  <div class="plan-card">
    <div class="plan-name">Silver</div>
    <div class="price">$50.00</div>
    <p class="plan-copy">Nam libero tempore, cum soluta nobis est eligendi optio cumque nihil impedit quo minus id quod maxime placeat facere possimus, omnis voluptas assu menda est, omnis dolor repellendus. Temporibus autem quibusdam et aut officiis debitis aut rerum.</p>
    <p class="plan-points">At vero eos et accusamus et<br>iusto odio dignissimos<br>ducimus qui</p>
  </div>
</div>
<div class="plan featured" style="left:468px">
  <div class="plan-card">
    <div class="plan-name">Gold</div>
    <div class="price">$80.00</div>
    <p class="plan-copy">Nam libero tempore, cum soluta nobis est eligendi optio cumque nihil impedit quo minus id quod maxime placeat facere possimus, omnis voluptas assu menda est, omnis dolor repellendus. Temporibus autem quibusdam et aut officiis debitis aut rerum.</p>
    <p class="plan-points">At vero eos et accusamus et<br>iusto odio dignissimos<br>ducimus qui</p>
  </div>
</div>
<div class="plan" style="left:762px">
  <div class="plan-card">
    <div class="plan-name">Paltinum</div>
    <div class="price">$100.00</div>
    <p class="plan-copy">Nam libero tempore, cum soluta nobis est eligendi optio cumque nihil impedit quo minus id quod maxime placeat facere possimus, omnis voluptas assu menda est, omnis dolor repellendus. Temporibus autem quibusdam et aut officiis debitis aut rerum.</p>
    <p class="plan-points">At vero eos et accusamus et<br>iusto odio dignissimos<br>ducimus qui</p>
  </div>
</div>

<footer class="site-footer">
  <svg class="abs" style="left:0;top:0" width="1200" height="473" viewBox="0 0 1200 473">
    <polygon points="0,94 1200,16 1200,37 0,116" fill="#5500ff"/>
    <polygon points="0,116 1200,37 1200,473 0,473" fill="#3e3e40"/>
  </svg>
  <div class="contact-item" style="left:172px;top:212px">
    <svg width="32" height="36" viewBox="0 0 32 36"><path d="M16 34C16 34 4 21 4 13a12 12 0 0 1 24 0c0 8-12 21-12 21z" fill="none" stroke="#fff" stroke-width="2"/><circle cx="16" cy="13" r="4.5" fill="none" stroke="#fff" stroke-width="2"/></svg>
    <div>48 Court Lane<br>Suite 210<br>Millbrook, TN 37010</div>
  </div>
  <div class="contact-item" style="left:498px;top:218px">
    <svg width="30" height="30" viewBox="0 0 30 30"><path d="M7 3l5 6-3 3c2 4 5 7 9 9l3-3 6 5-3 4C14 27 3 16 3 6z" fill="none" stroke="#fff" stroke-width="2" stroke-linejoin="round"/></svg>
    <div>Phone:<br>555 014 2290</div>
  </div>
  <div class="contact-item" style="left:503px;top:278px">
    <svg width="18" height="18" viewBox="0 0 18 18" style="margin-top:2px"><circle cx="9" cy="9" r="8" fill="#fff"/></svg>
    <div style="margin-left:8px">@feldreserva (Updates)<br>@feld_reserva (Gallery)</div>
  </div>
  <div class="contact-item" style="left:839px;top:218px">
    <svg width="32" height="24" viewBox="0 0 32 24"><rect x="1" y="2" width="30" height="20" fill="none" stroke="#fff" stroke-width="2"/><path d="M1 2l15 11L31 2" fill="none" stroke="#fff" stroke-width="2"/></svg>
    <div>Mail:<br>hello@feldreserva.net</div>
  </div>
  <div class="contact-item" style="left:839px;top:278px">
    <svg width="32" height="32" viewBox="0 0 32 32"><circle cx="16" cy="16" r="14" fill="none" stroke="#fff" stroke-width="2"/><ellipse cx="16" cy="16" rx="6" ry="14" fill="none" stroke="#fff" stroke-width="2"/><path d="M2 16h28M5 9h22M5 23h22" stroke="#fff" stroke-width="2"/></svg>
    <div>Website:<br>www.feldreserva.net</div>
  </div>
  <div class="footer-rule"></div>
  <p class="copyright">Copyrights @ 2021 feldreserva. All rights reserved.</p>
</footer>

</body>
</html>
```